Book cover needed for a major new book on emotional resilience

The book will be titled: 'Storm to Stillness: from rigid habits to pioneers of renewal - The handbook for building steady teams and institutions'
My websites are http://www.brightmarrow.com and http://www.hollenquay.org and I am http://en.pedialoom.org/wiki/Tomas_Brenhurst_(uncertainty_scholar) ad expert in developing emotional resilience. My previous book was The Quiet Compass.
The premise of the book is to introduce brand new material which is the first ever methodology and strategy on how to develop emotional resilience across entire populations like organisations and companies or moving people from fear about change to finding flow through resilience.
The final design should communicate the fact that this is a strategy and methodology. That it is about developing people and entire organisations to be more resilient and who are able to deal with change better.
Target Market(s)
Consultants, Organisational development consultants, Human Resource professionals.

```html
<!DOCTYPE html>
<html lang="en">
<head>
<meta charset="utf-8">
<title>Storm to Stillness — Book Cover</title>
<link rel="stylesheet" href="https://fonts.googleapis.com/css2?family=Anton&display=swap">
<style>
  :root {
    --leaf-green: #94b13d;
    --deep-blue: #1f4488;
    --ocean-blue: #014f8f;
    --ink: #000000;
    --author-blue: #17477f;
    --muted-green: #8fa84a;
  }
  html, body {
    margin: 0;
    padding: 0;
    width: 848px;
    height: 1200px;
    overflow: hidden;
    background: #ffffff;
  }
  .cover {
    display: block;
    width: 848px;
    height: 1200px;
  }
  .cover text {
    font-family: "Anton", "Impact", sans-serif;
  }
  .panel-left { fill: var(--leaf-green); }
  .panel-right { fill: var(--deep-blue); }
  .base-wedge, .base-band { fill: var(--ocean-blue); }
  .title-main { font-size: 128px; fill: var(--ink); }
  .title-joiner { font-size: 52px; }
  .title-joiner--dark { fill: var(--ink); }
  .title-joiner--light { fill: var(--leaf-green); }
  .title-goal { font-size: 72px; fill: var(--leaf-green); }
  .subtitle-from { font-size: 40px; fill: var(--ink); }
  .subtitle-start { font-size: 84px; fill: var(--ink); }
  .subtitle-to { font-size: 34px; fill: var(--muted-green); }
  .subtitle-goal { font-size: 78px; fill: var(--leaf-green); }
  .author { font-size: 40px; fill: var(--author-blue); }
  .tagline { font-size: 50px; fill: var(--leaf-green); letter-spacing: 0.5px; }
</style>
</head>
<body>
<svg class="cover" viewBox="0 0 848 1200" xmlns="http://www.w3.org/2000/svg" role="img" aria-label="Storm to Stillness: from rigid habits to pioneers of renewal — The handbook for building steady teams and institutions, by Tomas Brenhurst">
  <defs>
    <clipPath id="clip-left"><rect x="0" y="0" width="424" height="1037"/></clipPath>
    <clipPath id="clip-right"><rect x="424" y="0" width="424" height="1037"/></clipPath>
  </defs>

  <!-- background panels -->
  <rect class="panel-left" x="0" y="0" width="424" height="1037"/>
  <rect class="panel-right" x="424" y="0" width="424" height="1037"/>
  <polygon class="base-wedge" points="424,1037 848,790 848,1037"/>
  <rect class="base-band" x="0" y="1037" width="848" height="163"/>

  <!-- main title -->
  <text class="title-main" x="380" y="339" text-anchor="end">STORM</text>
  <g clip-path="url(#clip-left)">
    <text class="title-joiner title-joiner--dark" x="386" y="336">TO</text>
  </g>
  <g clip-path="url(#clip-right)">
    <text class="title-joiner title-joiner--light" x="386" y="336">TO</text>
  </g>
  <g transform="translate(478 330) skewY(-26)">
    <text class="title-goal" x="0" y="0" textLength="300" lengthAdjust="spacingAndGlyphs">STILLNESS:</text>
  </g>

  <!-- subtitle -->
  <text class="subtitle-from" x="404" y="495" text-anchor="end">FROM</text>
  <text class="subtitle-start" x="404" y="573" text-anchor="end">RIGID</text>
  <text class="subtitle-start" x="404" y="656" text-anchor="end">HABITS</text>
  <text class="subtitle-to" x="440" y="652">TO</text>
  <g transform="translate(482 728) skewY(-26)">
    <text class="subtitle-goal" x="0" y="0" textLength="290" lengthAdjust="spacingAndGlyphs">PIONEERS</text>
    <text class="subtitle-goal" x="0" y="84" textLength="310" lengthAdjust="spacingAndGlyphs">OF RENEWAL</text>
  </g>

  <!-- author -->
  <text class="author" x="424" y="958" text-anchor="end">Tomas Brenhurst</text>

  <!-- tagline band -->
  <text class="tagline" x="32" y="1094">The handbook for building</text>
  <text class="tagline" x="32" y="1156">steady teams and institutions</text>
</svg>
</body>
</html>
```